Limbcraft Arbor Crew Bill Board Design

We are a high class full service tree company who specializes in artistic thinning and shaping of trees in Arizona. We want to re brand our company to catch our audiences attention and hook them into calling our company on the spot. We’ve been in business for 30 years and have never truly branded our company. We want our shirts trucks and billboards to match as well as our mailing advertisement so our clientele can recognize us immediately. We are starting with our billboard first and will be following with truck and shirt designs next. Attached is a example of what we are looking for and what we’ve had designed so far. This just isn’t good enough and needs revamped if at all posssible.
- Stencil

```html
<!DOCTYPE html>
<html lang="en">
<head>
<meta charset="utf-8">
<title>Limbcraft Arbor Crew Billboard</title>
<link rel="stylesheet" href="https://fonts.googleapis.com/css2?family=Cinzel:wght@500;600&family=Teko:wght@500;600&family=Dancing+Script:wght@500&display=swap">
<style>
  :root {
    --page: #7a7a7a;
    --panel: #1b1715;
    --green: #2bb23c;
    --green-bright: #34c447;
    --band: #25a83a;
    --orange: #e07a1f;
    --gold: #c8952f;
    --gold-light: #f0c75a;
    --white: #ffffff;
    --leaf-dark: #3f6b2a;
    --leaf-light: #8fb862;
    --sky: #a9c7e8;
  }
  * { margin: 0; padding: 0; box-sizing: border-box; }
  html, body { width: 1051px; height: 1200px; overflow: hidden; background: var(--page); }
  .billboard {
    position: absolute; left: 35px; top: 459px;
    width: 980px; height: 282px; overflow: hidden;
    background: var(--panel);
    box-shadow: 0 6px 14px rgba(0,0,0,.35);
  }
  .work-photo {
    position: absolute; left: 0; top: 0; width: 460px; height: 282px;
    background:
      radial-gradient(circle at 30% 20%, var(--sky) 0 12%, transparent 30%),
      linear-gradient(160deg, var(--leaf-light), var(--leaf-dark) 55%, #5a8a3a);
  }
  .panel-shape { position: absolute; inset: 0; }
  .planting-photo {
    position: absolute; left: 298px; top: 100px; width: 164px; height: 164px;
    border-radius: 50%;
    border: 4px solid var(--gold);
    background:
      radial-gradient(circle at 60% 25%, #6e9a45 0 22%, transparent 40%),
      linear-gradient(180deg, #8fb4d6 0 25%, #b7a48c 55%, #8b7358);
    box-shadow: 0 3px 8px rgba(0,0,0,.5);
  }
  .award-badge {
    position: absolute; left: 26px; top: 5px; width: 80px; height: 80px;
    border-radius: 50%;
    background: radial-gradient(circle, #1c1a17 0 58%, var(--gold-light) 60%, var(--gold) 100%);
  }
  .brand {
    position: absolute; left: 560px; top: 24px; width: 400px; text-align: center;
  }
  .brand-name {
    font-family: "Cinzel", serif; font-weight: 600; font-size: 23px;
    color: var(--green); letter-spacing: .3px; white-space: nowrap;
  }
  .brand-tagline {
    font-family: "Dancing Script", cursive; font-size: 21px; color: var(--white);
    margin-top: 2px; white-space: nowrap;
  }
  .divider {
    position: absolute; left: 517px; width: 380px; height: 1px;
    background: linear-gradient(90deg, transparent, #8a6a3a 30%, #8a6a3a 70%, transparent);
  }
  .divider.top { top: 103px; }
  .divider.bottom { top: 208px; }
  .headline {
    position: absolute; left: 480px; top: 110px; width: 454px; text-align: center;
    font-family: "Teko", sans-serif; font-weight: 600; font-size: 39px; line-height: 46px;
    letter-spacing: 0; white-space: nowrap;
  }
  .headline .line-one { color: var(--green-bright); display: block; }
  .headline .line-two {
    display: inline-block;
    background: linear-gradient(90deg, var(--orange), #b9a030 55%, var(--green-bright));
    -webkit-background-clip: text; background-clip: text; color: transparent;
  }
  .cta {
    position: absolute; left: 455px; top: 226px; width: 525px; height: 56px;
    display: flex; align-items: center; color: var(--white);
  }
  .cta-request {
    font-family: "Cinzel", serif; font-weight: 500; font-size: 15px; line-height: 19px;
    text-align: right; width: 156px; white-space: nowrap;
  }
  .cta-rule { width: 2px; height: 34px; background: var(--white); margin: 0 14px; }
  .cta-phone { display: flex; align-items: center; gap: 6px; }
  .cta-phone svg { width: 32px; height: 32px; }
  .cta-number {
    font-family: "Teko", sans-serif; font-weight: 600; font-size: 48px; line-height: 1;
    padding-top: 6px; letter-spacing: .5px; white-space: nowrap;
  }
</style>
</head>
<body>
  <div class="billboard">
    <div class="work-photo" role="img" aria-label="Photo of an arborist in a blue bucket lift pruning a green tree with a pole saw"></div>

    <svg class="panel-shape" viewBox="0 0 980 282" aria-hidden="true">
      <defs>
        <linearGradient id="edgeGlow" x1="0" y1="0" x2="0" y2="1">
          <stop offset="0" stop-color="#2bb23c"/>
          <stop offset="1" stop-color="#c8952f"/>
        </linearGradient>
      </defs>
      <path d="M404 0 C374 60 364 160 389 282" fill="none" stroke="url(#edgeGlow)" stroke-width="7"/>
      <path d="M412 0 C382 60 372 160 397 282 L980 282 L980 0 Z" fill="#1b1715"/>
      <path d="M452 226 H980 V282 H432 Q438 250 452 226 Z" fill="#25a83a"/>
    </svg>

    <div class="planting-photo" role="img" aria-label="Photo of a worker planting and staking a young tree in a gravel yard"></div>
    <div class="award-badge" role="img" aria-label="Award badge"></div>

    <div class="brand">
      <div class="brand-name">Limbcraft Arbor Crew</div>
      <div class="brand-tagline">Providing Expert Tree Care</div>
    </div>

    <div class="divider top"></div>
    <h1 class="headline">
      <span class="line-one">SCULPTING ARIZONA'S TREES</span>
      <span class="line-two">WITH ARTISTIC PRECISION</span>
    </h1>
    <div class="divider bottom"></div>

    <div class="cta">
      <div class="cta-request">REQUEST<br>A FREE ESTIMATE</div>
      <div class="cta-rule"></div>
      <div class="cta-phone">
        <svg viewBox="0 0 32 32" aria-hidden="true">
          <circle cx="16" cy="16" r="14" fill="none" stroke="#fff" stroke-width="2"/>
          <path d="M11 9.5c1-.8 2-.6 2.5.3l1.3 2.4c.4.8.2 1.5-.5 2l-.9.7c.8 1.8 2 3 3.8 3.8l.7-.9c.5-.7 1.2-.9 2-.5l2.4 1.3c.9.5 1.1 1.5.3 2.5-1 1.2-2.4 1.7-4 1.1-4-1.5-6.9-4.4-8.4-8.4-.6-1.6-.1-3 1.1-4z" fill="#fff"/>
        </svg>
        <span class="cta-number">602-555-0147</span>
      </div>
    </div>
  </div>
</body>
</html>
```